Thornfield Marsh, LLC Website

We are a small law firm in need of a website that contains the following:
1. Attractive main page
2. About us/attorney info for three people: Leonard Thornfield (attorney), Brent Marsh (attorney), and Melinda Carrow (legal assistant). We have bio's ready to submit.
3. Blog/video page. We'd like to post blogs and videos to help drive traffic
4. Multidistrict Litigation and Class Actions page, where we post information regarding active MDLs and Class actions that we are doing intake on.
Updates

Can you also please use the color "gold" in the design and logo? Thanks.

Industry/Entity Type

Legal

Coding

Coded - Design and coding required

Number of Pages Required

1 page

Colors
0054AA
0677BA
7BADD7
CADEEF
E8F1F8

Requirements
Must have
• 1. Attractive main page 2. About us/attorney info for three people: Leonard Thornfield (attorney), Brent Marsh (attorney), and Melinda Carrow (legal assistant). We have bio's ready to submit. 3. Blog/video page. We'd like to post blogs and videos to help drive traffic 4. Multidistrict Litigation and Class Actions page, where we post information regarding active MDLs and Class actions that we are doing intake on.

```html
<!DOCTYPE html>
<html lang="en">
<head>
<meta charset="utf-8">
<title>Thornfield Marsh, LLC</title>
<link href="https://fonts.googleapis.com/css2?family=Libre+Baskerville:wght@700&family=Montserrat:wght@400;500;600;700&family=Comfortaa:wght@400;600&display=swap" rel="stylesheet">
<style>
:root{
  --navy:#0a1a8c;
  --navy-deep:#0c0c36;
  --sky:#1eb4ff;
  --sky-text:#22a9ef;
  --ink:#111;
  --muted:#555;
  --paper:#fbfcfd;
  --footer:#f6f6f7;
  --line:#dcdcdc;
  --white:#fff;
}
*{margin:0;padding:0;box-sizing:border-box}
html,body{width:1200px;height:2560px;overflow:hidden}
body{position:relative;background:var(--paper);font-family:'Montserrat',sans-serif;color:var(--ink)}
.abs{position:absolute}
.serif{font-family:'Libre Baskerville',serif;font-weight:700}

/* header */
.header{left:0;top:0;width:1200px;height:83px;background:var(--white)}
.brand{left:141px;top:20px;display:flex;align-items:center;gap:10px}
.brand-mark{width:34px;height:34px;background:var(--navy)}
.brand-name{font-weight:700;font-size:19px;color:var(--navy)}
.nav{right:133px;top:32px;display:flex;gap:38px;font-size:13px;font-weight:500}

/* hero */
.hero{left:0;top:83px;width:1200px;height:602px;background:linear-gradient(100deg,#6a4a32 0%,#9a6c48 35%,#caa27a 55%,#8a5a36 78%,#3a2414 100%)}
.hero-title{left:0;top:200px;width:1200px;text-align:center;color:var(--white);font-size:58px;line-height:60px}
.hero-tag{left:0;top:334px;width:1200px;text-align:center;color:var(--sky-text);font-weight:700;font-size:29px}
.cta{left:472px;top:396px;width:256px;height:48px;background:var(--navy);color:var(--white);font-weight:700;font-size:14px;display:flex;align-items:center;justify-content:center}
.hero-text{left:0;top:464px;width:1200px;text-align:center;color:var(--white);font-weight:600;font-size:16px;line-height:25px}
.hero-values{left:0;top:529px;width:1200px;text-align:center;color:var(--sky-text);font-weight:700;font-size:20px;word-spacing:4px}

/* practice */
.intro{left:0;top:759px;width:1200px;text-align:center;color:var(--muted);font-size:19.5px;line-height:29px}
.section-title{left:0;width:1200px;text-align:center;font-size:38px}
.area{top:922px;width:207px;height:203px;background:var(--white);border:1px solid var(--line);box-shadow:0 2px 6px rgba(0,0,0,.06);text-align:center}
.area svg{margin-top:26px}
.area-label{font-weight:500;font-size:20px;line-height:25px;margin-top:14px}

/* testimonials */
.band{left:0;top:1184px;width:1200px;height:461px;background:var(--sky)}
.quote{top:1262px;width:292px;height:229px;background:var(--white);border-radius:6px;padding:20px 18px}
.quote::after{content:"";position:absolute;left:26px;bottom:-9px;border:9px solid transparent;border-top-color:var(--white);border-bottom:0}
.quote h3{font-family:'Comfortaa',sans-serif;font-weight:600;font-size:17px;margin-bottom:12px}
.quote p{font-family:'Comfortaa',sans-serif;font-size:12px;line-height:20px;color:#555}
.client{top:1514px;display:flex;align-items:center;gap:13px;color:var(--white)}
.avatar{width:47px;height:47px;border-radius:50%;border:2px solid var(--white)}
.client b{display:block;font-size:15px;font-weight:700}
.client span{font-size:11px}

/* team */
.photo{top:1822px;width:214px;height:246px}

/* footer */
.footer{left:0;top:2208px;width:1200px;height:302px;background:var(--footer)}
.foot-brand{left:138px;top:2280px;color:var(--sky-text);font-weight:600;font-size:22px}
.foot-about{left:138px;top:2328px;width:222px;font-size:14px;line-height:23px;color:#333}
.foot-head{top:2280px;font-weight:600;font-size:15px}
.foot-list{list-style:none;font-size:14px;color:#333}
.foot-list li{height:27.5px}
.social li{display:flex;align-items:center;gap:9px;height:36.5px}
.email{left:850px;top:2373px;width:210px;height:40px;border:1px solid #8a8a9a;background:var(--white);font-size:11px;color:#999;padding:12px 12px}
.email svg{position:absolute;right:12px;top:10px}
.bottom{left:0;top:2510px;width:1200px;height:50px;background:var(--navy-deep)}
</style>
</head>
<body>

<header class="abs header">
  <div class="abs brand"><span class="brand-mark"></span><span class="brand-name">Thornfield Marsh, LLC</span></div>
  <nav class="abs nav"><span>Home</span><span>About Us</span><span>Blog</span><span>Our Team</span><span>Practice Areas</span><span>Contact Us</span></nav>
</header>

<section class="abs hero" role="img" aria-label="Bronze statue of Lady Justice holding scales in a softly lit courtroom"></section>
<h1 class="abs hero-title serif">The solution<br>to your legal matters.</h1>
<div class="abs hero-tag">Justice with Integrity</div>
<div class="abs cta">Request A Free Consultation</div>
<p class="abs hero-text">We Specialize in Multidistrict litigation and class actions.<br>Providing Dedicated repersentation for complex legal matters.</p>
<div class="abs hero-values">Experience&nbsp; . &nbsp;Dedication&nbsp; . &nbsp;Results</div>

<p class="abs intro">We are Resulte-driven law firm committed to<br>helping victims of corporate-negligence, defective products, and more.</p>
<h2 class="abs section-title serif" style="top:838px">Practice Areas</h2>

<div class="abs area" style="left:138px">
  <svg width="72" height="70" viewBox="0 0 72 70" fill="none" stroke-width="3" stroke-linejoin="round">
    <rect x="22" y="14" width="36" height="14" transform="rotate(-45 40 21)" stroke="#22a9ef"/>
    <line x1="40" y1="28" x2="64" y2="52" stroke="#22a9ef"/>
    <rect x="8" y="56" width="40" height="6" stroke="var(--navy)"/>
    <line x1="14" y1="50" x2="42" y2="50" stroke="var(--navy)"/>
  </svg>
  <div class="area-label">Class<br>Actions</div>
</div>
<div class="abs area" style="left:377px">
  <svg width="86" height="66" viewBox="0 0 86 66" fill="none" stroke-width="3">
    <rect x="26" y="4" width="34" height="60" stroke="var(--navy)"/>
    <rect x="4" y="22" width="22" height="42" stroke="var(--navy)"/>
    <rect x="60" y="22" width="22" height="42" stroke="var(--navy)"/>
    <g stroke="#22a9ef" stroke-width="2.5"><rect x="32" y="12" width="8" height="8"/><rect x="46" y="12" width="8" height="8"/><rect x="32" y="28" width="8" height="8"/><rect x="46" y="28" width="8" height="8"/><rect x="10" y="30" width="8" height="8"/><rect x="68" y="30" width="8" height="8"/></g>
    <rect x="37" y="48" width="12" height="16" stroke="var(--navy)"/>
  </svg>
  <div class="area-label">MDL<br>Ltigation</div>
</div>
<div class="abs area" style="left:617px">
  <svg width="60" height="68" viewBox="0 0 60 68" fill="none" stroke-width="3.5" stroke-linejoin="round">
    <path d="M30 4 L56 14 V34 C56 50 44 60 30 64 C16 60 4 50 4 34 V14 Z" stroke="var(--navy)"/>
    <path d="M19 34 L27 42 L42 26" stroke="#22a9ef" stroke-linecap="round"/>
  </svg>
  <div class="area-label">Consumer<br>Protection</div>
</div>
<div class="abs area" style="left:856px">
  <svg width="52" height="68" viewBox="0 0 52 68" fill="none" stroke-width="3.5">
    <circle cx="26" cy="18" r="9" stroke="#22a9ef"/>
    <path d="M4 62 C4 46 14 36 26 36 C38 36 48 46 48 62" stroke="var(--navy)" stroke-linecap="round"/>
  </svg>
  <div class="area-label">Personal<br>injury</div>
</div>

<section class="abs band"></section>
<div class="abs quote" style="left:144px"><h3>Incredible Experience</h3><p>We had an incredible experience working with Brightwell and were impressed they made such a big difference in only three weeks. Our team is so grateful for the wonderful improvements they made and their ability to get familiar with the concept so quickly.</p></div>
<div class="abs quote" style="left:458px"><h3>Incredible Experience</h3><p>We had an incredible experience working with Brightwell and were impressed they made such a big difference in only three weeks. Our team is so grateful for the wonderful improvements they made and their ability to get familiar with the concept so quickly.</p></div>
<div class="abs quote" style="left:764px"><h3>Incredible Experience</h3><p>We had an incredible experience working with Brightwell and were impressed they made such a big difference in only three weeks. Our team is so grateful for the wonderful improvements they made and their ability to get familiar with the concept so quickly.</p></div>

<div class="abs client" style="left:161px"><span class="avatar" role="img" aria-label="Client portrait" style="background:#6b4a38"></span><div><b>Nora Whitfield</b><span>CEO, Crestline Industries</span></div></div>
<div class="abs client" style="left:442px"><span class="avatar" role="img" aria-label="Client portrait" style="background:#c99a78"></span><div><b>Nora Whitfield</b><span>CEO, Crestline Industries</span></div></div>
<div class="abs client" style="left:716px"><span class="avatar" role="img" aria-label="Client portrait" style="background:#e6b7b8"></span><div><b>Nora Whitfield</b><span>CEO, Crestline Industries</span></div></div>

<h2 class="abs section-title serif" style="top:1727px">Meet Our Team</h2>
<div class="abs photo" style="left:143px;background:linear-gradient(160deg,#7a5a44,#3a2a22)" role="img" aria-label="Portrait of Leonard Thornfield, attorney, in a dark suit"></div>
<div class="abs photo" style="left:375px;background:linear-gradient(160deg,#2a2624,#141212)" role="img" aria-label="Portrait of Brent Marsh, attorney, in a dark suit"></div>
<div class="abs photo" style="left:609px;background:linear-gradient(160deg,#eef0f2,#cfd2d6)" role="img" aria-label="Portrait of team member in a black blazer"></div>
<div class="abs photo" style="left:842px;background:linear-gradient(160deg,#c9b79a,#6a6f78)" role="img" aria-label="Portrait of Melinda Carrow, legal assistant, in a grey blazer"></div>

<footer class="abs footer"></footer>
<div class="abs foot-brand">Web Agency</div>
<p class="abs foot-about">Lorem ipsum is placeholder text commonly used in the graphic, print, and publishing industries for previewing layouts and visual mockups.</p>

<div class="abs foot-head" style="left:378px">About</div>
<ul class="abs foot-list" style="left:376px;top:2323px"><li>About Us</li><li>Study Case</li><li>Blogs</li><li>Portfolio</li><li>careers</li></ul>

<div class="abs foot-head" style="left:612px">Follow Us</div>
<ul class="abs foot-list social" style="left:614px;top:2318px">
  <li><svg width="20" height="20" viewBox="0 0 20 20" fill="none" stroke="#22a9ef" stroke-width="1.5"><circle cx="10" cy="10" r="8"/></svg>fb.com/thornfieldmarsh</li>
  <li><svg width="20" height="20" viewBox="0 0 20 20" fill="none" stroke="#22a9ef" stroke-width="1.5"><rect x="2" y="2" width="16" height="16" rx="3"/></svg>@thornfieldmarsh</li>
  <li><svg width="20" height="20" viewBox="0 0 20 20" fill="none" stroke="#22a9ef" stroke-width="1.5"><circle cx="10" cy="10" r="8"/></svg>@thornfieldmarsh</li>
  <li><svg width="20" height="20" viewBox="0 0 20 20" fill="none" stroke="#22a9ef" stroke-width="1.5"><rect x="2" y="2" width="16" height="16"/></svg>thornfieldmarsh.example/news</li>
</ul>

<div class="abs foot-head" style="left:850px">Get In touch with Us</div>
<p class="abs" style="left:850px;top:2324px;font-size:13.5px;line-height:22px;color:#333">Need Answers? Need help ?<br>Just email us</p>
<div class="abs email">Your email
  <svg width="20" height="20" viewBox="0 0 20 20" fill="none" stroke="var(--navy)" stroke-width="1.5" stroke-linejoin="round"><path d="M2 9 L18 2 L12 18 L9 11 Z"/><path d="M9 11 L18 2"/></svg>
</div>

<div class="abs bottom"></div>
</body>
</html>
```